Natural Sunscreen Label Design for a Natural Cosmetics brand

We are looking to create a label design for a Natural Sunscreen Lotion. The labels will be a stick-on label on a white background tube. Enclosed a file with the content and some ideas/references. Please feel free to explore more.

It is important that the SPF is highlighted as large text and to use colors that give the customer an impression this being a sunscreen from far away as well.
We like white and orange/amber/yellow.
Details attached
Our Logo is attached as well as the size template of the label.

```html
<!DOCTYPE html>
<html lang="en">
<head>
<meta charset="utf-8">
<title>Marvento Natural Sunscreen – Label</title>
<link rel="stylesheet" href="https://fonts.googleapis.com/css2?family=Fira+Sans+Condensed:wght@400;500;600&family=Fira+Mono:wght@500&display=swap">
<style>
  :root {
    --bg: #dedfe1;
    --blue-deep: #0b5688;
    --blue-mid: #4a7fa9;
    --blue-soft: #6b97bb;
    --panel: #f1f2f3;
    --band: #0b5f96;
    --white: #ffffff;
    --label-top: #1b7cbc;
    --label-mid: #6f87b0;
    --label-lilac: #a99fb3;
    --label-sand: #e9ceb0;
  }
  html, body {
    margin: 0;
    width: 1200px;
    height: 800px;
    overflow: hidden;
    background: var(--bg);
  }
  .label {
    position: absolute;
    left: 397px;
    top: 35px;
    width: 406px;
    height: 730px;
    background:
      linear-gradient(90deg, rgba(255,255,255,0.22) 0%, rgba(255,255,255,0) 40%, rgba(0,40,90,0.12) 100%),
      linear-gradient(180deg, var(--label-top) 0%, #1a6ea9 38%, var(--label-mid) 62%, var(--label-lilac) 78%, var(--label-sand) 95%);
    font-family: "Fira Sans Condensed", sans-serif;
  }
  .panel {
    position: absolute;
    left: 75px;
    top: 37px;
    width: 256px;
    height: 693px;
    background: var(--panel);
    border-radius: 128px 128px 0 0;
  }
  .brand {
    position: absolute;
    top: 100px;
    left: 0;
    width: 100%;
    display: flex;
    justify-content: center;
    align-items: center;
    gap: 8px;
    color: var(--blue-deep);
    font-weight: 600;
    font-size: 22px;
    letter-spacing: 3px;
  }
  .brand-dot {
    width: 16px;
    height: 16px;
    border-radius: 50%;
    background: var(--blue-deep);
  }
  .copy { position: absolute; left: 21px; right: 10px; }
  .line-name {
    top: 230px;
    font-family: "Fira Mono", monospace;
    font-size: 19px;
    color: var(--blue-soft);
    letter-spacing: 1px;
  }
  .product-title {
    top: 263px;
    margin: 0;
    font-size: 35px;
    line-height: 37px;
    font-weight: 600;
    color: var(--blue-deep);
    letter-spacing: -0.5px;
  }
  .product-sub { top: 337px; font-size: 15px; color: var(--blue-soft); }
  .spf-label { top: 366px; font-size: 18px; color: var(--blue-mid); font-weight: 500; }
  .spf-value {
    top: 378px;
    font-size: 60px;
    line-height: 70px;
    font-weight: 500;
    color: var(--blue-mid);
    letter-spacing: -1px;
  }
  .spf-plus { color: var(--blue-deep); font-weight: 600; }
  .spf-range { top: 434px; font-size: 19px; color: var(--blue-deep); font-weight: 500; }
  .age-badge {
    position: absolute;
    left: 148px;
    top: 449px;
    width: 60px;
    text-align: center;
    color: var(--blue-mid);
    font-size: 10px;
    line-height: 12px;
  }
  .age-icon {
    width: 40px;
    height: 34px;
    margin: 4px auto;
    border-radius: 50%;
    background: #cfe0ee;
  }
  .water { top: 541px; font-size: 16px; color: var(--blue-mid); }
  .ingredients {
    top: 567px;
    font-size: 13px;
    line-height: 16px;
    color: var(--blue-deep);
    font-weight: 500;
  }
  .volume {
    position: absolute;
    right: 10px;
    top: 630px;
    font-size: 14px;
    color: var(--blue-deep);
  }
  .footer-band {
    position: absolute;
    left: 0;
    bottom: 0;
    width: 100%;
    height: 35px;
    background: var(--band);
    color: var(--white);
    font-size: 14px;
    letter-spacing: 3.4px;
    line-height: 35px;
    text-align: center;
    font-weight: 500;
  }
</style>
</head>
<body>
  <div class="label">
    <div class="panel">
      <div class="brand"><span class="brand-dot"></span><span>SOLBRISA</span></div>

      <div class="copy line-name">Marvento</div>
      <h1 class="copy product-title">NATURAL<br>SUNSCREEN</h1>
      <div class="copy product-sub">PROTETOR SOLAR</div>
      <div class="copy spf-label">SPF</div>
      <div class="copy spf-value">30<span class="spf-plus">+</span></div>
      <div class="copy spf-range">UVA+UVB</div>

      <div class="age-badge">
        <div>SAFE FOR</div>
        <div class="age-icon" role="img" aria-label="Baby icon for the safe-from-6-months badge"></div>
        <div>6 MONTHS</div>
      </div>

      <div class="copy water">WATER RESISTANT</div>
      <div class="copy ingredients">Made with organic Aloe Vera, Shea<br>Butter, Olive Oil, Roship Oil, Jojoa Oil<br>and Evening Primrosa Oil</div>
      <div class="volume">100 ml</div>

      <div class="footer-band">SOLBRISA - PORTUGAL</div>
    </div>
  </div>
</body>
</html>
```